Brookvale Auto Hire- car rental & accident claim management

We need a web design for a company based in Sydney called "Brookvale Auto Hire". We are a rental car company, who also specialise in not at fault accident claim management. when a client is not at fault in an accident, if they can provided us with the At Fault Parties (AFP) insurance details and claim number we can provide them with a rental car whilst their car is repaired (or if it is a total loss) and claim the costs of the rental car from the AFP's insurance company.
-rental vehicles
-accident repalcement vehicles
-third party recovery
-independent assessments
Our fleet comprises of small to large vehicles, including SUV's 4WD's, Prestige and commercial.
Our companies colour is bright green, so we would like it to be in keeping with that. we have two logo's. we would prefer the web page to use a bright/lime green (brighther than our logo).
we would ask that our design communicates quality, commitment to customer service and make our clients feel safe.
our competitors include: Meridian Recoveries and TKL if you would like to peruse these companies to get an idea of our industry. (tkl.example.au and meridianrecoveries.example.au)
Requirements
Must have
- telephone number to come. we are in the middle of chaniging so please leave space for the new phone number (once allocated to us) thank you

```html
<!DOCTYPE html>
<html lang="en">
<head>
<meta charset="utf-8">
<title>Brookvale Auto Hire</title>
<link href="https://fonts.googleapis.com/css2?family=Arimo:wght@400;700&display=swap" rel="stylesheet">
<style>
:root{
  --top-bar:#454545;
  --header-a:#f0f4cf;
  --header-b:#dde8a2;
  --lime:#8fd318;
  --page:#e8ecd9;
  --white:#ffffff;
  --text:#3d3d3d;
  --dark:#1f2a12;
  --green-dark:#4c9a0c;
  --green-mid:#6cb51f;
  --orange:#e8a21c;
  --gold:#f3cf3a;
  --footer-a:#7ccd00;
  --footer-b:#4ea405;
  --divider:#c9ea9a;
  --social-blue:#2f8fd0;
}
*{margin:0;padding:0;box-sizing:border-box}
html,body{width:1146px;height:1200px;overflow:hidden}
body{position:relative;font-family:"Arimo",Arial,sans-serif;color:var(--text);background:var(--page)}
.abs{position:absolute}
.top-bar{left:0;top:0;width:1146px;height:8px;background:var(--top-bar)}
.header{left:0;top:8px;width:1146px;height:109px;background:linear-gradient(180deg,var(--header-a),var(--header-b))}
.lime-band{left:0;top:117px;width:1146px;height:321px;background:var(--lime)}
.brand{left:150px;top:48px;display:flex;align-items:center;gap:8px;font-size:20px;font-weight:700;color:var(--green-dark);line-height:1.05}
.brand .mark{width:14px;height:14px;border-radius:50%;background:var(--green-dark)}
.phone{left:772px;top:24px;display:flex;align-items:center;gap:4px;font-size:20px;color:var(--green-dark)}
.social{display:flex;gap:4px}
.social span{width:14px;height:14px;border-radius:2px;background:var(--social-blue)}
.social span.rss{background:var(--orange)}
.phone .social{margin-left:8px}
.search{left:765px;top:61px;width:211px;height:26px;background:var(--white);border:1px solid #d6dcc0;font-size:10px;color:#444;padding:7px 8px}
.search .btn{position:absolute;right:0;top:0;width:26px;height:24px;background:#dcdcd2}
.search svg{position:absolute;right:7px;top:6px}
.nav{left:137px;top:117px;width:867px;height:40px;background:linear-gradient(180deg,#fff,#eef0ea);font-size:12.5px;color:#4a4a4a}
.nav a{position:absolute;top:13px;color:inherit;text-decoration:none;white-space:nowrap}
.nav a.active{left:8px;top:1px;width:61px;height:38px;background:var(--green-mid);color:var(--white);display:flex;align-items:center;justify-content:center}
.slider{left:137px;top:158px;width:867px;height:364px;background:var(--white);box-shadow:0 6px 6px -4px rgba(0,0,0,.35)}
.slide-photo{left:4px;top:5px;width:858px;height:298px;background:linear-gradient(180deg,#b9c4b2 0%,#7f8d60 40%,#8e8c85 70%,#b9b8b3 100%)}
.slide-caption{left:23px;top:309px;font-size:21px;line-height:26px;color:var(--orange)}
.dots{left:742px;top:324px;display:flex;gap:10px}
.dots span{width:16px;height:16px;border-radius:50%;background:var(--orange)}
.dots span.on{background:var(--green-mid);border:2px solid #e6f2d0}
.col-title{top:539px;font-size:16px;font-weight:400;color:#222;text-align:center;width:260px}
.rule{left:137px;top:563px;width:867px;height:1px;background:#dfe3cf}
.pic{border:1px solid #444}
.copy{font-size:10.6px;line-height:16.3px;color:var(--text)}
.big-phone{left:145px;top:795px;font-size:16px;font-weight:700;color:#333}
.more{width:103px;height:21px;border-radius:3px;border:1px solid #3f7d0a;background:linear-gradient(180deg,#94cc45,#4e9a11);color:var(--white);font-size:11px;display:flex;align-items:center;justify-content:center}
.footer{left:0;top:898px;width:1146px;height:212px;background:linear-gradient(180deg,var(--footer-a),var(--footer-b))}
.f-head{font-size:13px;font-weight:700;color:var(--dark)}
.f-list{list-style:none;font-size:10px;line-height:18px;color:var(--white)}
.f-list li{position:relative}
.f-list.links li::before{content:"»";position:absolute;left:-18px;color:var(--orange)}
.f-list.gold{color:var(--gold);font-weight:700}
.divider{top:922px;width:1px;height:147px;background:var(--divider)}
.bottom{left:0;top:1110px;width:1146px;height:90px;background:var(--white)}
.bottom-brand{left:140px;top:1150px;display:flex;align-items:center;gap:6px;font-size:12px;font-weight:700;color:#555}
.bottom-brand .mark{width:10px;height:10px;border-radius:50%;background:#888}
.bottom-nav{left:0;top:1124px;width:1146px;height:14px;font-size:10.5px;color:var(--green-mid)}
.bottom-nav span{position:absolute;top:0;white-space:nowrap}
.copyright{left:244px;top:1172px;font-size:9.5px;color:#333}
.partner{top:1170px;font-size:12px;font-weight:700;color:#444;white-space:nowrap}
</style>
</head>
<body>
<div class="abs top-bar"></div>
<div class="abs header"></div>
<div class="abs lime-band"></div>

<div class="abs brand"><span class="mark"></span><span>Brookvale<br>Auto Hire</span></div>

<div class="abs phone">
  <svg width="26" height="26" viewBox="0 0 26 26" aria-hidden="true"><circle cx="13" cy="13" r="11.5" fill="none" stroke="#222" stroke-width="2"/><path d="M9 7c1 0 2 2 2 3s-1 1-1 2 2 4 3 4 1-1 2-1 3 1 3 2-1 2-3 2c-4 0-8-5-8-9 0-2 1-3 2-3z" fill="#222"/></svg>
  <span>: 123-456-789</span>
  <span class="social"><span></span><span></span><span class="rss"></span></span>
</div>
<div class="abs search">Search our site<span class="btn"></span><svg width="12" height="12" viewBox="0 0 12 12" aria-hidden="true"><circle cx="5" cy="5" r="3.5" fill="none" stroke="#444" stroke-width="1.5"/><path d="M7.5 7.5l3.5 3.5" stroke="#444" stroke-width="1.8"/></svg></div>

<nav class="abs nav">
  <a class="active" href="#">Home</a>
  <a href="#" style="left:84px">Claim Form</a>
  <a href="#" style="left:161px">Partners</a>
  <a href="#" style="left:221px">Why Choose us</a>
  <a href="#" style="left:318px">Testimonials</a>
  <a href="#" style="left:395px">Services</a>
  <a href="#" style="left:448px">FAQs</a>
  <a href="#" style="left:491px">Contact Us</a>
  <a href="#" style="left:567px">News</a>
  <a href="#" style="left:612px">Client Login</a>
</nav>

<section class="abs slider">
  <div class="abs slide-photo" role="img" aria-label="Tow truck loading a damaged sedan on a roadside while two workers in high-visibility vests talk"></div>
  <div class="abs slide-caption">Rental Vehicles<br>Accident Replacement Vehicles</div>
  <div class="abs dots"><span class="on"></span><span></span><span></span><span></span></div>
</section>

<h2 class="abs col-title" style="left:111px">Replacement Car</h2>
<h2 class="abs col-title" style="left:452px">Rental Vehicle</h2>
<h2 class="abs col-title" style="left:738px">Accident Management</h2>
<div class="abs rule"></div>

<div class="abs" role="img" aria-label="Red sedan" style="left:155px;top:590px;width:210px;height:110px;background:radial-gradient(ellipse at center,#c8202a 0%,#9c1a20 45%,rgba(232,236,217,0) 72%)"></div>
<p class="abs copy" style="left:145px;top:716px;width:290px">Our Accident Management service will provide you with an accident replacement car and claim the cost from the at faultinsurer. Our Vehicles include Havrend, Quillmark, Solvane &amp; Dorrick.</p>
<div class="abs big-phone">123 456 789</div>
<div class="abs more" style="left:301px;top:856px">read more..</div>

<div class="abs pic" role="img" aria-label="Street map with a monitor and a red pickup truck" style="left:478px;top:570px;width:194px;height:137px;background:linear-gradient(135deg,#eeeeea,#d9dad4 60%,#c9c4b8)"></div>
<p class="abs copy" style="left:470px;top:713px;width:250px">Keep up to date with your claim online. View the progression of your claim through our website Reduces the need for in-house claims teams Offers seamless, effective and efficient solutions, designed to dovetail into your processes<br><br>Call Our 24/7 dedicated contact centre offering first class sales &amp; support services</p>
<div class="abs more" style="left:586px;top:856px">read more..</div>

<div class="abs pic" role="img" aria-label="Driver sitting beside a crashed car" style="left:767px;top:571px;width:201px;height:117px;background:linear-gradient(90deg,#8f949a,#5d636b 55%,#2e3238)"></div>
<p class="abs copy" style="left:758px;top:700px;width:260px">When your employees are behind the wheel, it is reassuring for you to know that they have the support of a comprehensive and robust Accident Manage-ment service if they are involved in an accident.<br><br>In today's fleet environment, such a service must not only meet the Health and Safety, Corporate Social Responsibility and Duty of Care demands, but also provide training facilities, extensive reporting and detailed risk consultations to help reduce your com-panies exposure and the</p>
<div class="abs more" style="left:901px;top:865px">read more..</div>

<footer class="abs footer"></footer>
<div class="abs f-head" style="left:172px;top:916px">Links</div>
<ul class="abs f-list links" style="left:172px;top:935px">
  <li>Home</li><li>Claim Form</li><li>Partners</li><li>Why Choose us</li><li>Testimonials</li><li>Services</li><li>FAQs</li><li>Contact Us</li><li>News</li>
</ul>
<div class="abs divider" style="left:352px"></div>
<div class="abs f-head" style="left:398px;top:917px">News</div>
<ul class="abs f-list" style="left:398px;top:936px;font-size:9.5px">
  <li>Lorem ipsum dolor sit amet</li><li><b>August 18th, 2009</b></li>
  <li>Lorem ipsum dolor sit amet</li><li><b>August 18th, 2009</b></li>
  <li>Lorem ipsum dolor sit amet</li><li><b>August 18th, 2009</b></li>
</ul>
<div class="abs divider" style="left:576px"></div>
<div class="abs f-head" style="left:622px;top:915px">Our Services</div>
<ul class="abs f-list gold" style="left:622px;top:936px;font-size:10.5px">
  <li>Replacement Car</li><li>Rental Vehicle</li><li>Accident Management</li>
  <li style="margin-top:10px">Replacement Car</li><li>Rental Vehicle</li><li>Accident Management</li>
</ul>
<div class="abs divider" style="left:812px"></div>
<div class="abs f-head" style="left:854px;top:919px">Contact</div>
<div class="abs" style="left:855px;top:957px;font-size:12px;font-weight:700;color:var(--gold)">BROOKVALE AUTO HIRE</div>
<ul class="abs f-list" style="left:855px;top:974px;font-weight:700;font-size:9.5px">
  <li>Address1 Address1 Address1</li><li>Ph: 123456789</li><li>Fax: 123456789</li>
</ul>
<div class="abs social" style="left:856px;top:1057px"><span></span><span></span><span class="rss"></span></div>

<div class="abs bottom"></div>
<div class="abs bottom-brand"><span class="mark"></span><span>Brookvale Auto Hire</span></div>
<div class="abs copyright">© 2012,Brookvale Auto Hire . All Rights Reserved.</div>
<div class="abs bottom-nav">
  <span style="left:406px">Home</span>
  <span style="left:461px">Claim Form</span>
  <span style="left:527px">Partners</span>
  <span style="left:578px">Why Choose us</span>
  <span style="left:661px">Testimonials</span>
  <span style="left:727px">Services</span>
  <span style="left:772px">FAQs</span>
  <span style="left:810px">Contact Us</span>
  <span style="left:875px">News</span>
  <span style="left:913px">Client Login</span>
</div>
<div class="abs partner" style="left:470px">Wrenfield Finance Partners</div>
<div class="abs partner" style="left:666px">Havrend</div>
<div class="abs partner" style="left:736px">Solvane</div>
<div class="abs partner" style="left:806px">Dorrick</div>
<div class="abs partner" style="left:864px">Kestova</div>
</body>
</html>
```